I am looking to create a newly designed website for our national leadership conference which is entitled, "The Lantern Path Leadership Summit". The Lantern Path Leadership Summit is a national conference for student leaders that prepares them for career leadership success. The current website can be seen at www.lanternpathleadershipsummit.com.

My goal for the new site is to create a more updated, fresh, hip, and exciting look that appeals to the younger generation while also maintaining are professional appeal. The color should be black, white, and gold. We want there to be live videos played and places to insert pictures for the panels as well.

I look forward to seeing you the new creations.

Number of Pages Required

1 page

Requirements
Must have
• Ability to play videos on the home page and throughout the website. Also, make sure that the website shows up clearly on an iPhone.
Nice to have
• Nice look

```html
<!DOCTYPE html>
<html lang="en">
<head>
<meta charset="utf-8">
<title>Contact | The Lantern Path Leadership Summit</title>
<link href="https://fonts.googleapis.com/css2?family=Roboto:wght@300;400;500;700&display=swap" rel="stylesheet">
<style>
:root{
  --gold:#b98f3d;
  --gold-light:#d8b46a;
  --ink:#222;
  --text:#555;
  --band:#f3f3f4;
  --dark:#262626;
  --dark-2:#1c1c1c;
  --muted:#8a8a8a;
  --white:#fff;
}
*{box-sizing:border-box;margin:0;padding:0}
html,body{width:730px;height:1200px;overflow:hidden;background:var(--white);font-family:"Roboto",Arial,sans-serif;color:var(--ink)}
.page{position:relative;width:730px;height:1200px}
.abs{position:absolute}
a{color:inherit;text-decoration:none}

.follow{left:46px;top:29px;display:flex;align-items:center;gap:3px;font-size:7px;font-weight:500}
.follow span{margin-right:3px}
.social{width:16px;height:16px;background:#9a9a9a;display:inline-block}
.brand{left:290px;top:18px;width:150px;text-align:center}
.brand-dot{width:14px;height:14px;border-radius:50%;background:var(--gold);margin:0 auto 8px}
.brand-name{font-size:10px;font-weight:700;letter-spacing:1.3px;color:var(--ink)}
.btn-gold{background:linear-gradient(var(--gold-light),var(--gold));color:var(--white);border-radius:20px;text-align:center;font-weight:500}
.register{left:550px;top:21px;width:135px;height:32px;line-height:32px;font-size:13px}

.nav{left:0;top:76px;width:730px;height:37px;background:linear-gradient(#3a3a3a,var(--dark-2));display:flex;padding-left:93px}
.nav a{color:var(--white);font-size:8.5px;font-weight:500;line-height:37px;padding:0 14px}
.nav a.active{background:linear-gradient(var(--gold-light),var(--gold))}

.crumb{left:50px;top:134px;font-size:7px;color:#666}
.crumb b{color:var(--gold);font-weight:400}

.band{left:0;width:730px;background:var(--band)}
.band-title{left:92px;font-size:14px;font-weight:500;letter-spacing:.5px;line-height:17px}
.band-title em{font-style:normal;color:var(--gold);display:block}
.marker{display:inline-block;width:10px;height:10px;border-radius:50%;background:var(--gold)}
.arrow{font-size:18px;color:#222}
.logos{display:flex;align-items:center;justify-content:space-around}
.partner{display:flex;align-items:center;gap:5px;font-size:11px;font-weight:500;color:#555}
.chip{width:10px;height:10px;border-radius:50%;background:#bdbdbd}

.heading{font-size:15px;font-weight:500;letter-spacing:.4px;display:flex;align-items:center;gap:10px}
.heading em{font-style:normal;color:var(--gold)}

.photo{width:108px;height:107px;border-radius:16px}
.person{width:185px}
.person h3{font-size:10px;font-weight:500;color:var(--gold);letter-spacing:.3px;margin-bottom:8px}
.person p{font-size:9px;font-weight:300;color:var(--text);line-height:14.5px;margin-bottom:6px}
.person a{font-size:7.5px;font-weight:500;display:flex;align-items:center;gap:8px}

.form{left:46px;top:697px;width:639px;height:253px;background:var(--dark);border-radius:18px}
.form .heading{color:var(--white)}
.field{background:var(--white);border-radius:14px;font-size:7.5px;color:#777;padding:0 16px;line-height:24px;height:24px}
.msg{height:84px;border-radius:16px;padding-top:8px;line-height:12px}
.submit{left:219px;top:199px;width:201px;height:39px;line-height:39px;font-size:16px}

.timer{width:45px;height:48px;background:#222;border:2px solid #555;border-radius:3px;color:var(--gold-light);text-align:center}
.timer b{display:block;font-size:22px;font-weight:500;line-height:30px}
.timer span{display:block;font-size:6px;color:var(--white)}

.footer{left:0;top:1088px;width:730px;height:112px;background:var(--dark)}
.foot-nav{left:46px;top:37px;display:flex;gap:18px;font-size:7.5px;color:var(--white);font-weight:500}
.legal{left:46px;top:63px;font-size:7px;color:#aaa;line-height:13px}
.foot-brand{left:570px;top:40px;width:120px;text-align:center}
.foot-brand .brand-dot{background:#666}
.foot-brand .brand-name{color:#777}
</style>
</head>
<body>
<div class="page">
  <header>
    <div class="abs follow"><span>FOLLOW US</span><i class="social"></i><i class="social"></i><i class="social"></i><i class="social"></i><i class="social"></i></div>
    <div class="abs brand"><div class="brand-dot"></div><div class="brand-name">LANTERN PATH</div></div>
    <a class="abs btn-gold register" href="#">REGISTER NOW</a>
  </header>
  <nav class="abs nav">
    <a href="#">HOME</a><a class="active" href="#">ABOUT</a><a href="#">CONFERENCE</a><a href="#">REGISTER</a><a href="#">TESTIMONIALS</a><a href="#">Y FACTOR</a><a href="#">VIDEOS</a><a href="#">CONTACT</a>
  </nav>
  <div class="abs crumb">HOME &raquo; <b>CONTACT</b></div>

  <section class="abs band" style="top:153px;height:81px">
    <i class="abs marker" style="left:62px;top:36px"></i>
    <div class="abs band-title" style="top:25px">NETWORK WITH<em>EXECUTIVES</em></div>
    <div class="abs arrow" style="left:231px;top:28px">&lsaquo;</div>
    <div class="abs logos" style="left:248px;top:22px;width:422px;height:38px">
      <div class="partner"><i class="chip"></i>Arcline</div>
      <div class="partner"><i class="chip"></i>Bayford</div>
      <div class="partner"><i class="chip"></i>Tonehouse</div>
      <div class="partner"><i class="chip"></i>Korvant</div>
      <div class="partner"><i class="chip"></i>Pennyroll</div>
    </div>
    <div class="abs arrow" style="left:676px;top:28px">&rsaquo;</div>
  </section>

  <h2 class="abs heading" style="left:316px;top:262px"><i class="marker"></i><span>CONTACT <em>US</em></span></h2>

  <div class="abs photo" role="img" aria-label="Portrait photo of Marisa Delgado" style="left:46px;top:310px;background:linear-gradient(#b9a489,#6e5a48)"></div>
  <div class="abs person" style="left:168px;top:328px"><h3>MARISA DELGADO</h3><p>Vice President Of Conference Logistics And Student Engagement</p><a href="#">&#9993; Email Marisa</a></div>
  <div class="abs photo" role="img" aria-label="Portrait photo of Tessa Moreland" style="left:384px;top:310px;background:linear-gradient(#8d9a7c,#2f3446)"></div>
  <div class="abs person" style="left:506px;top:328px"><h3>TESSA MORELAND</h3><p>Executive Assistant To Daniel Ashcroft, President</p><a href="#">&#9993; Email Tessa</a></div>
  <div class="abs photo" role="img" aria-label="Black and white portrait photo of Renee Whitfield" style="left:46px;top:445px;background:linear-gradient(#cfcfcf,#5a5a5a)"></div>
  <div class="abs person" style="left:168px;top:470px"><h3>RENEE WHITFIELD</h3><p>Director Of Campus Ambassadors</p><a href="#">&#9993; Email Renee</a></div>
  <div class="abs photo" role="img" aria-label="Portrait photo of Jolene Harper" style="left:384px;top:445px;background:linear-gradient(#f2f2f2,#4a3a3a)"></div>
  <div class="abs person" style="left:506px;top:463px"><h3>JOLENE HARPER</h3><p>Director Of Social Media</p><a href="#">&#9993; Email Jolene</a></div>

  <section class="abs band" style="top:596px;height:81px">
    <i class="abs marker" style="left:62px;top:36px"></i>
    <div class="abs band-title" style="top:16px">2015 CONFERENCE<em>PARTNERS AND<br>SUPPORTS</em></div>
    <div class="abs arrow" style="left:231px;top:28px">&lsaquo;</div>
    <div class="abs logos" style="left:248px;top:22px;width:422px;height:38px">
      <div class="partner"><i class="chip"></i>Westvale Power</div>
      <div class="partner"><i class="chip"></i>Kairo Motors</div>
      <div class="partner"><i class="chip"></i>Greenleaf</div>
      <div class="partner"><i class="chip"></i>Rojo Grill</div>
      <i class="chip" style="width:30px;height:30px"></i>
    </div>
    <div class="abs arrow" style="left:676px;top:28px">&rsaquo;</div>
  </section>

  <form class="abs form">
    <h2 class="abs heading" style="left:220px;top:22px"><i class="marker"></i><span>GENERAL <em>NFORMATION</em></span></h2>
    <div class="abs field" style="left:16px;top:66px;width:197px">Name</div>
    <div class="abs field" style="left:221px;top:66px;width:197px">School/Company</div>
    <div class="abs field" style="left:426px;top:66px;width:197px">Your Email</div>
    <div class="abs field msg" style="left:13px;top:99px;width:612px">Message</div>
    <div class="abs btn-gold submit">CONTACT US</div>
  </form>

  <h2 class="abs heading" style="left:218px;top:974px"><i class="marker"></i><span>6TH ANNUAL <em>CONFERENCE COUNTDOWN</em></span></h2>
  <div class="abs timer" style="left:276px;top:1015px"><b>0</b><span>HOURS</span></div>
  <div class="abs timer" style="left:343px;top:1015px"><b>0</b><span>MINUTES</span></div>
  <div class="abs timer" style="left:409px;top:1015px"><b>0</b><span>SECONDS</span></div>

  <footer class="abs footer">
    <div class="abs foot-nav"><a href="#">HOME</a><a href="#">ABOUT</a><a href="#">CONFERENCE</a><a href="#">REGISTER</a><a href="#">TESTIMONIALS</a><a href="#">Y FACTOR</a><a href="#">VIDEOS</a><a href="#">CONTACT</a></div>
    <div class="abs legal">Copyright &copy; 2015. Company Name All Right Reserved<br>Privacy Policy &nbsp;|&nbsp; Term &amp; Conditions</div>
    <div class="abs foot-brand"><div class="brand-dot"></div><div class="brand-name">LANTERN PATH</div></div>
  </footer>
</div>
</body>
</html>
```